B2B Tear Sheet / Flyer for Corvana Summit Partners

Design multiple creative treatments for a 1-page, 2-sided tear sheet/flyer for a B2B consulting firm called Corvana Summit Partners, targeting Private Equity firms, Family Offices, Investment Banks, and Independent Sponsors. This piece will be handed out at conferences, 1-on-1 meetings, and potential snail mail (direct mail) campaigns. Eventually, the piece could also be made available on our website. The company is in start-up mode, so our website is not yet up and working. But we do have a logo and color palette.

```html
<!DOCTYPE html>
<html lang="en">
<head>
<meta charset="utf-8">
<title>Corvana Summit Partners – Tear Sheet</title>
<link href="https://fonts.googleapis.com/css2?family=Red+Hat+Display:wght@500;700;800&family=Raleway:wght@300;400;500;600;700&display=swap" rel="stylesheet">
<style>
:root{
  --green-dark:#3c6a49;
  --green-mid:#4f8c5e;
  --green-light:#5d9c6c;
  --tab-grey:#e4e4e4;
  --ink:#222;
  --backdrop:#d6d6d6;
  --white:#fff;
}
*{box-sizing:border-box;margin:0;padding:0}
html,body{width:1200px;height:1117px;overflow:hidden}
body{background:var(--backdrop);font-family:'Raleway',sans-serif;color:var(--ink);position:relative}
.page{position:absolute;top:202px;width:551px;height:712px;background:var(--white);overflow:hidden}
.page--front{left:43px}
.page--back{left:609px}
.abs{position:absolute}
h1,h2,h3{font-family:'Red Hat Display',sans-serif}

/* front */
.front-header{left:0;top:0;width:398px;height:94px;background:var(--green-dark);color:var(--white);text-align:center;padding-top:16px}
.front-header h1{font-size:25px;font-weight:800;letter-spacing:-.2px;line-height:1.1}
.front-header p{font-size:13.5px;font-weight:300;line-height:1.1;margin-top:3px}
.brand{left:398px;top:0;width:153px;height:94px;display:flex;align-items:center;justify-content:center;gap:6px}
.brand__mark{width:10px;height:10px;background:var(--green-dark)}
.brand__name{font-size:12px;font-weight:600;color:var(--green-dark);line-height:1.15}
.green-field{left:0;top:100px;width:551px;height:190px;background:var(--green-dark)}
.strip{left:0;top:93px;width:413px;height:18px;background:var(--green-light);border-radius:0 9px 9px 0;color:var(--white);font-weight:700;font-size:9.6px;line-height:18px;padding-left:26px;font-family:'Red Hat Display',sans-serif}
.intro{left:26px;top:117px;width:506px;font-size:7.2px;line-height:8.6px;color:var(--white);text-align:justify}
.intro b{font-weight:700}
.wedges{left:0;top:0;width:551px;height:712px}
.box{left:26px;width:499px;background:var(--white);border:2px solid var(--green-dark);border-radius:13px}
.pill{position:absolute;left:6px;right:6px;top:4px;height:22px;border-radius:11px;background:linear-gradient(90deg,var(--green-dark),var(--green-mid) 50%,var(--green-dark));color:var(--white);text-align:center;font-weight:700;font-size:10.5px;line-height:22px;font-family:'Red Hat Display',sans-serif}
.divider{position:absolute;width:1px;background:#555}
ul.ticks{list-style:none}
ul.ticks li{position:relative;padding-left:11px;font-size:7.6px;line-height:9.65px}
ul.ticks li::before{content:"";position:absolute;left:1px;top:2.6px;border-left:4px solid #333;border-top:2.3px solid transparent;border-bottom:2.3px solid transparent}
.subtab{position:absolute;top:29px;height:20px;background:var(--tab-grey);font-weight:700;font-size:8.6px;line-height:20px;text-align:center;font-family:'Red Hat Display',sans-serif}
.lead{font-size:8.6px;line-height:10.5px}
.lead--green{color:var(--green-dark);font-weight:700}
.bottom-band{left:26px;top:608px;width:499px;height:21px;background:var(--green-light);border-radius:0 0 12px 12px;color:var(--white);font-weight:700;font-size:8.6px;text-align:center;line-height:23px;font-family:'Red Hat Display',sans-serif}
.band-notch{left:269px;top:628px;width:0;height:0;border-left:6px solid transparent;border-right:6px solid transparent;border-top:6px solid var(--green-light)}
.benefits{top:640px}
.benefits ul.ticks li{font-size:7.6px;line-height:8.8px;margin-bottom:9px}

/* back */
.back-tab{left:0;top:0;width:260px;height:50px;background:var(--green-dark);border-radius:0 0 18px 0;color:var(--white);font-size:20.5px;font-weight:800;padding:14px 0 0 22px}
.photo-founder{left:272px;top:0;width:279px;height:207px;background:linear-gradient(120deg,#e9ecef,#c9d3dc 55%,#8ea3bd)}
.reasons{left:22px;top:60px;width:238px;font-size:7.3px;line-height:9.05px;text-align:justify}
.reasons p+p{margin-top:9px}
.founder{left:272px;top:213px;width:279px;height:163px;background:var(--green-dark);color:var(--white);padding:12px 14px 0 12px}
.founder h2{font-size:18.5px;font-weight:800;margin-bottom:3px}
.founder p{font-size:7.2px;line-height:8.55px;text-align:justify}
.office{left:0;top:520px;width:551px;height:150px;background:linear-gradient(180deg,#dcdcdc,#9a9a9a 55%,#c4c4c4)}
.mindset{left:26px;top:393px;width:497px;height:128px;background:var(--white);border:2px solid var(--green-dark);border-radius:13px}
.mindset .pill{height:28px;line-height:28px;font-size:18px;font-weight:800;border-radius:14px}
.mindset ul.ticks{position:absolute;left:20px;top:38px}
.mindset ul.ticks li{font-size:7.8px;line-height:10.8px}
.contact{left:0;top:669px;width:551px;height:43px;display:flex;font-family:'Red Hat Display',sans-serif;color:var(--white);font-weight:700}
.contact__label{width:155px;background:var(--green-light);font-size:14px;line-height:43px;text-align:center}
.contact__gap{width:5px;background:var(--white)}
.contact__details{flex:1;background:var(--green-dark);font-size:14px;display:flex;align-items:center;gap:8px;padding-left:16px}
.contact__details svg{flex:none}
</style>
</head>
<body>

<section class="page page--front">
  <div class="abs green-field"></div>
  <svg class="abs wedges" viewBox="0 0 551 712" aria-hidden="true">
    <polygon points="0,270 0,330 30,350 30,290" fill="#5d9c6c"/>
    <polygon points="551,270 551,330 521,350 521,290" fill="#5d9c6c"/>
    <polygon points="0,560 0,600 30,580" fill="#3c6a49"/>
    <polygon points="551,560 551,600 521,580" fill="#3c6a49"/>
  </svg>
  <header class="abs front-header">
    <h1>Corvana Summit Partners</h1>
    <p>Fractional Marketing Services for Private Equity Funds,<br>Family Offices &amp; Investment Banks</p>
  </header>
  <div class="abs brand"><span class="brand__mark"></span><span class="brand__name">Corvana Summit Partners</span></div>
  <div class="abs strip">Fractional Marketing Services: The Alternative to a Full-Time Marketing Staff</div>
  <p class="abs intro">Hiring a full-time corporate marketing staff, or even a single marketing employee, can be an expensive proposition. Corvana Summit Partners provides <b>Part-Time Marketing</b> Services to middle market clients, which allow them to receive best-in-class corporate marketing at a fraction of the cost of a full-time Analyst or Associate, or even an entry-level Marketing Coordinator. <b>Fractional Marketing Services</b> have been used for years for <b>Private Equity</b> portfolio companies, but only recently have they been made available to <b>Private Equity Funds</b> themselves, <b>Family Offices,</b> and <b>Investment Banks.</b> When selecting a <b>Fractional Marketing Services</b> resource, prospective clients should ensure their <b>Fractional Chief Marketing Officer (CMO)</b> has broad firsthand <b>Private Equity</b> and <b>Banking</b> experience in the areas of Marketing, Business Development, Fundraising, and Principal Investing, which can be leveraged to quickly create differentiated marketing strategies and tactics, along with 21st Century tools to increase lead generation, deal flow, and stakeholder satisfaction.</p>

  <div class="abs box" style="top:193px;height:200px">
    <div class="pill">Fractional Marketing Services</div>
    <div class="subtab" style="left:0;width:222px;border-radius:0 10px 10px 0">Monthly Retained Marketing Services</div>
    <div class="subtab" style="left:274px;width:223px;border-radius:10px 0 0 10px">Marketing Audit &amp; Planning Services</div>
    <div class="divider" style="left:247px;top:36px;height:150px"></div>
    <div class="abs" style="left:18px;top:52px;width:220px">
      <p class="lead">Up to 20-Hours/Month</p>
      <p class="lead lead--green">Strategy, Management &amp; Execution</p>
      <ul class="ticks" style="margin-top:2px">
        <li>Press Release Drafting &amp; Distribution</li>
        <li>Email Campaigns &amp; Drip Marketing / Lead Nurturing</li>
        <li>Digital Marketing &amp; Advertising</li>
        <li>Content Development &amp; Collateral Management</li>
        <li>Website Analysis, Updates &amp; Remarketing</li>
        <li>SEO &amp; SEM•Dashboard &amp; KPIs</li>
        <li>Vendor Tool Selection &amp; Implementation</li>
        <li>List Management</li>
        <li>Go-to-Market Strategy</li>
        <li>Linkwise Enhancement &amp; Lead Gen</li>
        <li>Other Social Media</li>
        <li>Offline Activity Management</li>
      </ul>
    </div>
    <div class="abs" style="left:272px;top:52px;width:222px">
      <p class="lead lead--green">Assessment Areas</p>
      <ul class="ticks" style="margin-top:2px">
        <li>Website &amp; Traffic Analysis•SEO &amp; SEM</li>
        <li>Social Media (e.g., Linkwise, etc.)</li>
        <li>Email &amp; Other Digital</li>
        <li>Press Releases</li>
        <li>Collaterals</li>
        <li>Content Management / CMS</li>
        <li>Generative chat tools and A.I.</li>
        <li>Advertising (if applicable)—all channels</li>
        <li>Full-Funnel Evaluation</li>
        <li>Biz Dev &amp; Marketing Integration</li>
        <li>CRM &amp; Data Integrity</li>
        <li>Creative Assessment</li>
        <li>Strategy, Messaging &amp; Marketing Plan (optional)</li>
      </ul>
    </div>
  </div>

  <div class="abs box" style="top:401px;height:88px">
    <div class="pill">Special Projects</div>
    <div class="divider" style="left:247px;top:38px;height:42px"></div>
    <ul class="ticks abs" style="left:18px;top:36px">
      <li>Branding &amp; Rebranding</li><li>Website Overhaul</li><li>Corporate Identity</li><li>Data Cleansing</li><li>Video Production &amp; Management</li>
    </ul>
    <ul class="ticks abs" style="left:270px;top:36px">
      <li>CRM Selection, Design &amp; Transition</li><li>Customer Intelligence Studies</li><li>Marketing Brainstorming &amp; Facilitation</li><li>Marketing Resource Evaluation</li><li>Boards of Directors</li>
    </ul>
  </div>

  <div class="abs box" style="top:497px;height:115px;border-radius:13px 13px 0 0;border-bottom:none">
    <div class="pill">New Fund Launch Services</div>
    <div class="divider" style="left:247px;top:36px;height:72px"></div>
    <ul class="ticks abs" style="left:18px;top:34px">
      <li>For Inaugural &amp; Follow-on Funds</li><li>6 &amp; 12-Month Project</li><li>Limited Availability</li><li>Fees based on fund size, number, stage &amp; complexity</li>
    </ul>
    <div class="abs" style="left:16px;top:78px;width:206px;border-top:1px solid #555"></div>
    <p class="abs lead lead--green" style="left:16px;top:83px;width:206px;text-align:center;line-height:10px">New Fund Launch Services can commence<br>before or during fundraising</p>
    <ul class="ticks abs" style="left:270px;top:34px">
      <li>Includes all Fractional Marketing Services (above)</li><li>Plus: Website creation or overhaul</li><li>Plus: CRM design &amp; implementation</li><li>Plus: Corporate identity work</li><li>Plus: Social media &amp; digital launch</li><li>Plus: Marketing Audit for follow-on funds</li><li>Plus: Business development and GTM strategy</li>
    </ul>
  </div>
  <div class="abs bottom-band">With Corvana Summit Partners Fractional Marketing Services, you can:</div>
  <div class="abs band-notch"></div>

  <ul class="ticks abs benefits" style="left:40px;width:130px">
    <li>Receive Best-in-Class Marketing strategies &amp; tactics for a fraction of the cost of an Analyst</li>
    <li>Leverage the experience of a 17+ year middle market Private Equity Chief Marketing Officer</li>
  </ul>
  <div class="divider abs" style="left:187px;top:641px;height:62px"></div>
  <ul class="ticks abs benefits" style="left:199px;width:150px">
    <li>No benefits or payroll taxes</li>
    <li style="margin-top:19px">No need to stay knowledgeable on marketing and lead generation tactics, which change daily</li>
  </ul>
  <div class="divider abs" style="left:358px;top:641px;height:62px"></div>
  <ul class="ticks abs benefits" style="left:370px;width:150px">
    <li>100% remote, with onsite work from time-to-time and at your discretion</li>
    <li>Receive LP-friendly reports to prove your differentiation and ensure their satisfaction</li>
  </ul>
</section>

<section class="page page--back">
  <svg class="abs wedges" viewBox="0 0 551 712" aria-hidden="true">
    <path d="M150,388 Q280,360 420,388 Z" fill="#5d9c6c"/>
    <polygon points="0,420 0,470 30,450 30,410" fill="#5d9c6c"/>
    <polygon points="551,420 551,470 521,450 521,410" fill="#5d9c6c"/>
    <rect x="0" y="380" width="551" height="140" fill="#3c6a49" opacity="0"/>
  </svg>
  <div class="abs office" role="img" aria-label="Soft grey photo of business people meeting in a bright office"></div>
  <svg class="abs wedges" viewBox="0 0 551 712" aria-hidden="true">
    <polygon points="0,400 551,400 551,520 0,520" fill="#3c6a49"/>
    <path d="M0,400 Q275,360 551,400 Z" fill="#ffffff"/>
    <polygon points="0,430 26,415 26,450 0,470" fill="#5d9c6c"/>
    <polygon points="551,430 525,415 525,450 551,470" fill="#ffffff"/>
    <path d="M160,400 Q280,372 410,400 Z" fill="#5d9c6c"/>
  </svg>
  <h2 class="abs back-tab">Our Reasons for Being</h2>
  <div class="abs photo-founder" role="img" aria-label="Photo of the founder smiling at his desk with a laptop"></div>
  <div class="abs reasons">
    <p>Today’s increasingly competitive environment for middle market <b>Private Equity Funds, Family Offices,</b> and <b>Investment Banks,</b> has left little time for those entities to focus on their <b>marketing</b> strategies, tactics, and execution. At best, a Business Development executive is forced to take on a Marketing role as a part-time, almost side job, taking valuable time away from their in-person deal origination responsibilities. At worst, a GP whose primary focus is on deal evaluation and execution, is forced to give up hours of their time trying to perform tasks in which they are not trained or updated in 21st Century marketing tactics. Marketing goes beyond Business Development but should work with it in an integrated manner to ensure a seamless connection between funds and their three primary target markets: Investors, Private Company Owners, and Deal Sources.</p>
    <p><b>Corvana Summit Partners</b> was created to bring <b>Fractional Marketing Services</b> to <b>Private Equity Funds</b> and <b>Family Offices</b> and the <b>Intermediaries</b> and <b>Counselors</b> who serve them. For years, the <b>Fractional Marketing</b> Services concept has been leveraged in <b>Private Equity,</b> but only for <b>Portfolio Companies,</b> with little <b>Corporate Marketing</b> attention given to the funds themselves. Finally, <b>Private Equity Funds, Family Offices,</b> and <b>Investment Banks</b> are realizing they are too busy competing to win the next deal and enhancing Portco equity value to be able to focus on a <b>Marketing</b> and <b>Lead Generation</b> system that is dynamic and ever-changing. At <b>Corvana Summit Partners,</b> we believe that roughly 1/3 of the skills required to be a successful B2B financial services marketer 10-years from now haven’t even been identified yet. Why not leave the execution of your critical marketing function to a firm that lives and breathes <b>Private Equity, Family Office,</b> and <b>Investment Bank Marketing</b> full-time? Contact us immediately for a <b>no obligation</b> discussion at <b>1.555.204.7318</b> or <b>DanH@CorvanaSummit.com.</b></p>
  </div>
  <div class="abs founder">
    <h2>Principal &amp; Founder</h2>
    <p>Daniel Hartwell has over 25 years of <b>Private Equity</b> experience, 17 of which have been spent as Chief Marketing Officer (CMO) for middle market <b>Private Equity funds.</b> As a past <b>General Partner,</b> his knowledge of <b>Private Equity</b> marketing, business development, fundraising, principal investing, and portfolio company enhancement, positions him unlike any other in the middle market: <b>“A Marketer with an Investor’s Mindset,”</b> Daniel has experience in buyouts, non-control/ mezzanine, growth equity, ABL, and venture capital asset classes. Unlike agency experienced marketers who operate without first hand <b>Private Equity</b> empathy, <b>Corvana Summit Partners</b> brings firsthand <b>PE</b> experience and knowledge of what GPs must accomplish with their marketing efforts to satisfy their three primary target markets: Investors, Company Owners, and Deal Sources.</p>
  </div>
  <div class="abs mindset">
    <div class="pill">A Marketer With An Investor’s Mindset</div>
    <ul class="ticks">
      <li>17-Years as Private Equity Chief Marketing Officer—one of the industry’s first</li>
      <li>25-Years total Private Equity experience, including Marketing, Business Development, Fundraising &amp; Principal Investing</li>
      <li>40-Years total Sales and Marketing experience, including Corporate and Global Strategy Consulting</li>
      <li>Experienced in most asset classes, including Buyouts, Growth Equity, Mezzanine, ABL and Venture</li>
      <li>More deal, business development, and marketing experienced than any Analyst or Associate, typically assigned to these roles</li>
      <li>Arguably, the most experienced middle market Private Equity marketer in the U.S.</li>
    </ul>
  </div>
  <div class="abs contact">
    <div class="contact__label">Contact us now:</div>
    <div class="contact__gap"></div>
    <div class="contact__details">
      <svg width="14" height="10" viewBox="0 0 14 10" aria-hidden="true"><rect x=".6" y=".6" width="12.8" height="8.8" fill="none" stroke="#fff" stroke-width="1.1"/><path d="M.8,.8 7,6 13.2,.8" fill="none" stroke="#fff" stroke-width="1.1"/></svg>
      <span>DanH@CorvanaSummit.com</span>
      <span style="font-weight:400;margin:0 4px">|</span>
      <svg width="13" height="13" viewBox="0 0 13 13" aria-hidden="true"><circle cx="6.5" cy="6.5" r="5.8" fill="none" stroke="#fff" stroke-width="1.1"/><path d="M4.3,3.4c-.6.5-.5,1.6.5,3s2.4,2.6,3.3,2.4l.7-.8-1.2-1-.6.4c-.5-.2-1.2-.9-1.4-1.4l.4-.6-1-1.2z" fill="#fff"/></svg>
      <span>1.555.204.7318</span>
    </div>
  </div>
</section>

</body>
</html>
```